I would like a flyer for the ultimate masquarade ball. This will be a PARTY! We need a flyer that will jump out and catch the attention of anyone who sees it. We would like plenty of purple and gold to be used in the flyer. The final design should communicate the ultmate, upscale, classy, exciting masquarade ball ever!

This flyer must be designed for high resolution for printing on 4" x 6" flyers.

Industry/Entity Type

Printing

Requirements
Must have
• Rho Kappa Chapter Presents
Sigma Violet & Amber Masquerade Gala
1 March 2014
8pm - 1am
3-Course Plated Dinner
Cash Bar
RSVP By: 28 Feb 2014
Halvorsen Gaming & Downs, Larkspur Banquet Hall
DJ Tarvek
Details & Tickets: http://sigmavioletambergala.ticketlark.example
More Info? 555-317-8826
Dress Code: Black Tie & Traditional Dress, Costumes & Masks Preferred

```html
<!DOCTYPE html>
<html lang="en">
<head>
<meta charset="utf-8">
<title>Sigma Violet &amp; Amber Masquerade Gala</title>
<link rel="stylesheet" href="https://fonts.googleapis.com/css2?family=Titan+One&family=Montserrat:wght@700&family=Marcellus&family=Open+Sans:wght@600;700&family=Allura&family=Arimo:wght@400;700&display=swap">
<style>
  :root {
    --ink: #050307;
    --violet: #6a1b8f;
    --violet-deep: #3a0b52;
    --violet-bright: #8e2bb8;
    --gold: #e6b94c;
    --gold-light: #f6d98a;
    --gold-band: #d69a1e;
    --white: #ffffff;
  }
  html, body {
    margin: 0;
    padding: 0;
    width: 851px;
    height: 1200px;
    overflow: hidden;
    background: var(--ink);
  }
  .flyer {
    position: relative;
    width: 851px;
    height: 1200px;
    overflow: hidden;
    background:
      radial-gradient(ellipse 520px 640px at 760px 330px, rgba(106,27,143,0.85), rgba(58,11,82,0.45) 55%, rgba(5,3,7,0) 80%),
      var(--ink);
    color: var(--gold);
    text-align: center;
  }
  .mask-art {
    position: absolute;
    left: 360px;
    top: 0;
    width: 491px;
    height: 760px;
    background: radial-gradient(ellipse at 60% 45%, rgba(142,43,184,0.55), rgba(106,27,143,0.25) 50%, rgba(5,3,7,0) 75%);
  }
  .swoosh {
    position: absolute;
    left: 0;
    top: 860px;
    width: 851px;
    height: 340px;
  }
  .mask-art-small {
    position: absolute;
    left: 0;
    top: 960px;
    width: 170px;
    height: 130px;
    background: radial-gradient(ellipse at 40% 50%, rgba(180,90,210,0.55), rgba(106,27,143,0) 70%);
  }
  .line {
    position: absolute;
    left: 0;
    width: 851px;
    margin: 0;
    white-space: nowrap;
  }
  .presenter {
    top: 34px;
    font-family: "Titan One", sans-serif;
    font-size: 25px;
    color: var(--white);
    letter-spacing: 0.5px;
  }
  .event-title {
    top: 96px;
    font-family: "Montserrat", sans-serif;
    font-weight: 700;
    font-size: 47px;
    letter-spacing: 6px;
    color: var(--gold);
  }
  .event-subtitle {
    top: 140px;
    font-family: "Marcellus", serif;
    font-size: 92px;
    line-height: 1;
    letter-spacing: 1px;
    background: linear-gradient(180deg, #fff6dc, #e9c97a);
    -webkit-background-clip: text;
    background-clip: text;
    -webkit-text-fill-color: transparent;
  }
  .flourish {
    position: absolute;
    left: 280px;
    top: 238px;
    width: 330px;
    height: 34px;
    background: radial-gradient(ellipse at center, rgba(255,255,255,0.55), rgba(255,255,255,0.1) 55%, rgba(255,255,255,0) 75%);
  }
  .venue {
    font-family: "Open Sans", sans-serif;
    font-weight: 700;
    font-size: 37px;
    color: var(--gold);
    letter-spacing: 0.3px;
  }
  .venue-name { top: 288px; }
  .venue-hall { top: 336px; }
  .date-time {
    top: 391px;
    font-family: "Open Sans", sans-serif;
    font-weight: 700;
    font-size: 28px;
    color: var(--gold);
  }
  .photo-frames {
    position: absolute;
    left: 0;
    top: 430px;
    width: 851px;
    height: 270px;
  }
  .dj {
    top: 722px;
    font-family: "Allura", cursive;
    font-size: 82px;
    color: var(--white);
    text-shadow: 0 0 1px #fff, 0 0 1px #fff;
  }
  .offer {
    font-family: "Open Sans", sans-serif;
    font-weight: 700;
    font-size: 32px;
    color: var(--gold);
  }
  .offer-dinner { top: 828px; }
  .offer-bar { top: 874px; }
  .divider-ornament {
    position: absolute;
    left: 375px;
    top: 930px;
    width: 100px;
    height: 14px;
    background: radial-gradient(ellipse at center, rgba(255,255,255,0.6), rgba(255,255,255,0) 70%);
  }
  .rsvp {
    position: absolute;
    left: 535px;
    top: 969px;
    width: 330px;
    height: 46px;
    border-radius: 6px;
    background: var(--violet-deep);
    font-family: "Open Sans", sans-serif;
    font-weight: 700;
    font-size: 21px;
    line-height: 46px;
    color: var(--white);
    text-align: left;
    padding-left: 22px;
    box-sizing: border-box;
  }
  .tickets-label {
    top: 1050px;
    font-family: "Open Sans", sans-serif;
    font-weight: 700;
    font-size: 27px;
    color: var(--gold);
  }
  .tickets-contact {
    top: 1086px;
    font-family: "Open Sans", sans-serif;
    font-weight: 600;
    font-size: 25px;
    letter-spacing: 1.4px;
    color: var(--gold);
  }
  .dress-code {
    position: absolute;
    left: 0;
    top: 1125px;
    width: 851px;
    height: 75px;
    background: linear-gradient(180deg, var(--gold-band), #c98a12);
    font-family: "Arimo", sans-serif;
    font-size: 20px;
    letter-spacing: 0.7px;
    line-height: 54px;
    color: #000;
    text-align: center;
  }
  .dress-code strong { font-weight: 700; }
</style>
</head>
<body>
  <main class="flyer">
    <div class="mask-art" role="img" aria-label="Large purple masquerade mask illustration in the background"></div>

    <svg class="swoosh" viewBox="0 0 851 340" aria-hidden="true">
      <defs>
        <linearGradient id="swooshFill" x1="0" y1="0" x2="1" y2="0">
          <stop offset="0" stop-color="#5b1479"/>
          <stop offset="0.6" stop-color="#3a0b52"/>
          <stop offset="1" stop-color="#7a1fa3"/>
        </linearGradient>
      </defs>
      <path d="M0 40 C 260 150, 560 170, 851 10 L 851 340 L 0 340 Z" fill="url(#swooshFill)"/>
    </svg>
    <div class="mask-art-small" role="img" aria-label="Small purple masquerade mask illustration"></div>

    <p class="line presenter">Rho Kappa Chapter Presents</p>
    <h1 class="line event-title">SIGMA VIOLET &amp; AMBER</h1>
    <p class="line event-subtitle">Masquerade Gala</p>
    <div class="flourish" role="img" aria-label="White ornamental flourish divider"></div>

    <p class="line venue venue-name">HALVORSEN GAMING &amp; DOWNS</p>
    <p class="line venue venue-hall">LARKSPUR BANQUET HALL</p>
    <p class="line date-time">1 March 2014 • 8pm - 1am</p>

    <svg class="photo-frames" viewBox="0 430 851 270" aria-hidden="true">
      <g fill="#d99a25">
        <ellipse cx="150" cy="565" rx="113" ry="132"/>
        <ellipse cx="331" cy="565" rx="113" ry="132"/>
        <ellipse cx="512" cy="565" rx="113" ry="132"/>
        <ellipse cx="693" cy="565" rx="113" ry="132"/>
      </g>
      <g fill="#ffffff">
        <ellipse cx="150" cy="565" rx="108" ry="127"/>
        <ellipse cx="331" cy="565" rx="108" ry="127"/>
        <ellipse cx="512" cy="565" rx="108" ry="127"/>
        <ellipse cx="693" cy="565" rx="108" ry="127"/>
      </g>
    </svg>

    <p class="line dj">DJ Tarvek</p>
    <p class="line offer offer-dinner">3-Course Plated Dinner</p>
    <p class="line offer offer-bar">Cash Bar</p>
    <div class="divider-ornament" role="img" aria-label="Small white scroll ornament"></div>

    <div class="rsvp">RSVP By: 28 Feb 2014</div>

    <p class="line tickets-label">Details &amp; Tickets</p>
    <p class="line tickets-contact">sigmavioletambergala.ticketlark.example • 555-317-8826</p>

    <footer class="dress-code"><strong>Dress Code</strong> Black Tie &amp; Traditional Dress, Costumes &amp; Masks Preferred</footer>
  </main>
</body>
</html>
```